iron deficiency anemia - educational reference paper

looking for an educational paper/poster 8x11 or no larger than 11x14 that lists the most common foods with pictures and limited words a super rough outline attached - I wrote the words of the pictures (but would like to have the actual pictures of these items) I would like in roughly the same order
for the pictures for fatigue, headache....can be drawings or cartoons
double sided or single sided (which ever fits) see attached for categories (3 of them)

Target Market(s)

educational for people with limited education - thus not much wording

Requirements
Must have
• pictures, simple design

```html
<!DOCTYPE html>
<html lang="en">
<head>
<meta charset="utf-8">
<title>Iron Deficiency Anemia – Reference Sheets</title>
<link rel="stylesheet" href="https://fonts.googleapis.com/css2?family=Lato:ital,wght@0,700;1,700;1,900&family=Oswald:wght@600&display=swap">
<style>
  :root{
    --backdrop:#585858;
    --paper:#ffffff;
    --teal:#0e8a7c;
    --teal-light:#12a596;
    --maroon:#6e1416;
    --maroon-dark:#4e0d0f;
    --ink:#2b2b2b;
  }
  *{box-sizing:border-box;margin:0;padding:0}
  html,body{width:1200px;height:1200px;overflow:hidden}
  body{background:var(--backdrop);position:relative;font-family:'Lato',Arial,sans-serif;color:var(--ink)}

  .sheet{position:absolute;top:217px;width:551px;height:707px;background:var(--paper);overflow:hidden;box-shadow:4px 6px 10px rgba(0,0,0,.35)}
  .sheet--foods{left:38px}
  .sheet--symptoms{left:607px}

  /* Foods sheet */
  .foods-title{position:absolute;top:5px;left:0;width:100%;text-align:center;font-style:italic;font-weight:700;font-size:31.5px;color:var(--teal);letter-spacing:-.3px}
  .foods-band{position:absolute;top:43px;left:0;width:100%;height:41px;background:linear-gradient(90deg,var(--maroon-dark),var(--maroon) 50%,var(--maroon-dark));color:#fff;font-family:'Oswald',Arial,sans-serif;font-weight:600;font-size:30.5px;line-height:41px;text-align:center;letter-spacing:.7px}
  .food-grid{position:absolute;top:89px;left:27px;width:515px;display:grid;grid-template-columns:132px 126px 127px 130px;grid-auto-rows:42.5px}
  .food{display:flex;align-items:center;gap:5px;font-weight:700;font-size:12.5px;line-height:1}
  .food-photo{flex:none;width:50px;height:33px}
  .food-row-last{position:absolute;top:650px;left:0;width:100%}
  .food-row-last .food{position:absolute;top:0;gap:10px}
  .foods-foot{position:absolute;bottom:0;left:0;width:100%;height:15px;background:var(--maroon-dark)}

  /* Symptoms sheet */
  .rule{position:absolute;left:0;width:100%;height:4px;top:46px;border-top:1.5px solid var(--maroon);border-bottom:1.5px solid var(--maroon)}
  .symptoms-pill{position:absolute;top:16px;left:128px;width:304px;height:60px;border-radius:30px;background:var(--teal);color:#fff;font-style:italic;font-weight:700;font-size:31px;line-height:58px;text-align:center}
  .symptom{position:absolute;width:130px;height:130px;margin:-65px 0 0 -60px}
  .symptom-ring{position:absolute;left:0;top:0}
  .symptom-label{position:absolute;transform:translateX(-50%);white-space:nowrap;font-style:italic;font-weight:900;font-size:20px;color:var(--ink)}
  .wave{position:absolute;left:0;top:0}
  .signs-title{position:absolute;top:402px;left:0;width:100%;text-align:center;font-style:italic;font-weight:700;font-size:31px;color:#fff}
  .signs-line{position:absolute;top:423px;height:1.5px;background:#fff}
  .sign{position:absolute;width:130px;height:130px;margin:-65px 0 0 -65px;border-radius:50%;background:#fff;padding:3px}
  .sign-photo{width:100%;height:100%;border-radius:50%}
</style>
</head>
<body>

<section class="sheet sheet--foods">
  <h1 class="foods-title">Iron Deficiency Anemia</h1>
  <h2 class="foods-band">COMMON FOODS IN YOUR COMMUNITY</h2>

  <div class="food-grid">
    <div class="food"><div class="food-photo" role="img" aria-label="Photo of sheep in a field" style="background:linear-gradient(#7da35a,#5f8a40 45%,#dcd6c4 60%,#5f8a40)"></div>Sheep/lamb</div>
    <div class="food"><div class="food-photo" role="img" aria-label="Photo of a goose on grass" style="background:radial-gradient(ellipse 30% 40% at 45% 45%,#8a8478,#8aa56a 80%)"></div>Goose</div>
    <div class="food"><div class="food-photo" role="img" aria-label="Photo of a whale in the ocean" style="background:linear-gradient(160deg,#5a8ac4,#1c3a66 50%,#2b5f9a)"></div>Whale</div>
    <div class="food"><div class="food-photo" role="img" aria-label="Photo of winged beans" style="background:linear-gradient(100deg,#2c6a25,#5aa842 40%,#2c6a25 70%,#4e9a36)"></div>Winged bean</div>

    <div class="food"><div class="food-photo" role="img" aria-label="Photo of a bowl of rice bran" style="background:radial-gradient(ellipse 45% 40% at 50% 45%,#d8bf8e,#a27a46 70%,#e6dccc)"></div>Rice bran</div>
    <div class="food"><div class="food-photo" role="img" aria-label="Photo of white beans in a bowl" style="background:radial-gradient(ellipse 45% 45%,#f4efe6,#e2d8ca 60%,#b88a6c 80%)"></div>White bean</div>
    <div class="food"><div class="food-photo" role="img" aria-label="Photo of a pig" style="background:radial-gradient(ellipse 40% 45%,#f0c0b0,#d89a8a 60%,#7a5a44)"></div>Pig/pork</div>
    <div class="food"><div class="food-photo" role="img" aria-label="Photo of kidney beans" style="background:radial-gradient(ellipse 45% 45%,#9b2a3a,#7a1e2c 60%,#e4d8d8)"></div>Kidney bean</div>

    <div class="food"><div class="food-photo" role="img" aria-label="Photo of cowpeas" style="background:radial-gradient(circle,#f4ead8,#dcc8a6 70%,#fff)"></div>Cowpea</div>
    <div class="food"><div class="food-photo" role="img" aria-label="Photo of black beans in a bowl" style="background:radial-gradient(ellipse 45% 45%,#2c2c3a,#1a1a24 60%,#d8d8d8)"></div>Black bean</div>
    <div class="food"><div class="food-photo" role="img" aria-label="Photo of mung beans" style="background:radial-gradient(ellipse 50% 50%,#9aa452,#6a742e 70%,#d8d8d0)"></div>Mung bean</div>
    <div class="food"><div class="food-photo" role="img" aria-label="Photo of natto with chopsticks" style="background:radial-gradient(ellipse 45% 40% at 50% 60%,#c8a064,#8a6a44 60%,#3a2e24)"></div>Natto</div>

    <div class="food"><div class="food-photo" role="img" aria-label="Photo of teff grain with a scoop" style="background:radial-gradient(ellipse 45% 40% at 50% 60%,#b0764a,#7a4a2c 70%,#f0ece4)"></div>Teff</div>
    <div class="food"><div class="food-photo" role="img" aria-label="Photo of amaranth grain" style="background:linear-gradient(#f2ead8,#e0c890 55%,#c9a868)"></div>Amaranth</div>
    <div class="food"><div class="food-photo" role="img" aria-label="Photo of yardlong beans" style="background:linear-gradient(100deg,#3d7a26,#6ab842 30%,#3d7a26 60%,#6ab842)"></div>Yardlong Bean</div>
    <div class="food"><div class="food-photo" role="img" aria-label="Photo of a bowl of pink beans" style="background:radial-gradient(ellipse 45% 35% at 50% 40%,#a4624e,#d8c8c0 70%,#eeeae6)"></div>Chili/pink Bean</div>

    <div class="food"><div class="food-photo" role="img" aria-label="Photo of lentils in a wooden bowl" style="background:radial-gradient(ellipse 48% 40%,#8a8070,#6a5444 70%,#fff 90%)"></div>Lentil</div>
    <div class="food"><div class="food-photo" role="img" aria-label="Photo of yellow beans" style="background:radial-gradient(circle,#f0d040,#d0a41a 70%,#b08414)"></div>Yellow bean</div>
    <div class="food"><div class="food-photo" role="img" aria-label="Photo of a duck on water" style="background:linear-gradient(#b8cad4,#9fb6c4 40%,#3d5a3a 55%,#7a8a9a)"></div>Duck</div>
    <div class="food"><div class="food-photo" role="img" aria-label="Photo of lima beans" style="background:radial-gradient(ellipse 50% 50%,#b4dc84,#7ab052 70%,#e8ece4)"></div>Lima bean</div>

    <div class="food"><div class="food-photo" role="img" aria-label="Photo of chickens" style="background:linear-gradient(#6a9a44,#6a3a24 60%,#4a6a2a)"></div>Chicken</div>
    <div class="food"><div class="food-photo" role="img" aria-label="Photo of clams" style="background:radial-gradient(ellipse 40% 40%,#a88a70,#d8cfc4 70%,#eeeae4)"></div>Clams</div>
    <div class="food"><div class="food-photo" role="img" aria-label="Photo of pumpkin seeds" style="background:linear-gradient(90deg,#a8b86a,#c0c880 50%,#b8665a)"></div>Pumpkin Seed</div>
    <div class="food"><div class="food-photo" role="img" aria-label="Photo of squab birds" style="background:linear-gradient(120deg,#2e2e2a,#9a9890 50%,#4a4a44)"></div>Squab</div>

    <div class="food"><div class="food-photo" role="img" aria-label="Photo of pigeon peas" style="background:radial-gradient(circle,#e8c09a,#c8925e 70%,#f4eee6)"></div>Pigeon Pea</div>
    <div class="food"><div class="food-photo" role="img" aria-label="Photo of fava beans" style="background:radial-gradient(ellipse 50% 50%,#74cc40,#3e8a1e 80%)"></div>Fava Bean</div>
    <div class="food"><div class="food-photo" role="img" aria-label="Photo of sesame seeds" style="background:linear-gradient(90deg,#ece4d0,#d8cca8 35%,#2c3040 60%,#a09078)"></div>Sesame Seed</div>
    <div class="food"><div class="food-photo" role="img" aria-label="Photo of adzuki beans" style="background:radial-gradient(ellipse 40% 40% at 40% 60%,#8a2e24,#3a2420 70%,#2a1a18)"></div>Adzuki bean</div>

    <div class="food"><div class="food-photo" role="img" aria-label="Photo of cranberry beans" style="background:linear-gradient(120deg,#8a2a3a,#c87a84 40%,#e4d4c8)"></div>Cranberry bean</div>
    <div class="food"><div class="food-photo" role="img" aria-label="Photo of masa flatbreads" style="background:radial-gradient(circle at 35% 50%,#f0c49a,#e8a06a 40%,#2c3a5a)"></div>Masa</div>
    <div class="food"><div class="food-photo" role="img" aria-label="Photo of split peas" style="background:radial-gradient(circle,#8ac440,#5a962a 80%)"></div>Split Peas</div>
    <div class="food"><div class="food-photo" role="img" aria-label="Photo of cuttlefish" style="background:linear-gradient(130deg,#3a8a8a,#7a5a6a 50%,#4a6a7a)"></div>Cuttlefish bear</div>

    <div class="food"><div class="food-photo" role="img" aria-label="Photo of sunflower seeds" style="background:radial-gradient(circle at 55% 20%,#f0c01a,#4a4030 50%,#8a8070)"></div>Sunflower Seed</div>
    <div class="food"><div class="food-photo" role="img" aria-label="Photo of a bagel" style="background:radial-gradient(circle,#6a4a2c 10%,#c8945a 30%,#8a6240 70%)"></div>Bagel</div>
    <div class="food"><div class="food-photo" role="img" aria-label="Photo of sardines" style="background:repeating-linear-gradient(120deg,#2a3a5a 0 4px,#9aaac4 4px 8px)"></div>Sardines</div>
    <div class="food"><div class="food-photo" role="img" aria-label="Photo of chickpeas in a bowl" style="background:radial-gradient(ellipse 48% 45%,#e8b04a,#c08a2a 75%,#fff)"></div>Chickpeas</div>

    <div class="food"><div class="food-photo" role="img" aria-label="Photo of shrimp" style="background:linear-gradient(120deg,#4a3428,#8a6248 50%,#4a3428)"></div>Shrimp</div>
    <div class="food"><div class="food-photo" role="img" aria-label="Photo of spinach leaves" style="background:radial-gradient(ellipse 45% 45%,#3a8a3a,#2a6a2a 60%,#e0ece0)"></div>Spinach</div>
    <div class="food"><div class="food-photo" role="img" aria-label="Photo of beets" style="background:radial-gradient(circle at 60% 60%,#6a1a34,#4a1224 40%,#c8c0b4)"></div>Beet</div>
    <div class="food"><div class="food-photo" role="img" aria-label="Photo of Brussels sprout plants" style="background:linear-gradient(90deg,#3a5a28,#6a9a4a 50%,#3a5a28)"></div>Brussel sprout</div>

    <div class="food"><div class="food-photo" role="img" aria-label="Photo of eggs" style="background:radial-gradient(circle at 40% 55%,#f0aa6a,#d07a3e 50%,#8a5a34)"></div>Egg</div>
    <div class="food"><div class="food-photo" role="img" aria-label="Photo of collard greens" style="background:linear-gradient(130deg,#3a6a2e,#6a9a5a 50%,#d0d4c8)"></div>Collard greens</div>
    <div class="food"><div class="food-photo" role="img" aria-label="Photo of mushrooms" style="background:radial-gradient(circle,#ece0d0,#b89a7a 60%,#6a4a34)"></div>Mushroom</div>
    <div class="food"><div class="food-photo" role="img" aria-label="Photo of mixed nuts" style="background:radial-gradient(circle,#c8a070,#8a6240 60%,#4a3224)"></div>Nuts</div>

    <div class="food"><div class="food-photo" role="img" aria-label="Photo of potatoes" style="background:radial-gradient(ellipse 40% 45% at 55% 50%,#d8b064,#a07a3a 50%,#2a2018)"></div>Potato</div>
    <div class="food"><div class="food-photo" role="img" aria-label="Photo of tortillas" style="background:radial-gradient(circle at 45% 45%,#f2e0bc,#d8b888 60%,#e8e8e8)"></div>Tortilla</div>
    <div class="food"><div class="food-photo" role="img" aria-label="Photo of a turkey" style="background:radial-gradient(ellipse 40% 45%,#3a3028,#4a4a34 60%,#7a8a5a)"></div>Turkey</div>
    <div class="food"><div class="food-photo" role="img" aria-label="Photo of blackberries" style="background:radial-gradient(ellipse 50% 40% at 50% 35%,#2a2034,#3a3048 60%,#e0e0e4)"></div>Blackberry</div>

    <div class="food"><div class="food-photo" role="img" aria-label="Photo of broccoli" style="background:radial-gradient(circle,#5aaa44,#2e6a24 80%)"></div>Broccoli</div>
    <div class="food"><div class="food-photo" role="img" aria-label="Photo of carrots" style="background:repeating-linear-gradient(70deg,#f08a2a 0 6px,#d85a14 6px 10px)"></div>Carrot</div>
    <div class="food"><div class="food-photo" role="img" aria-label="Photo of cauliflower" style="background:radial-gradient(circle at 55% 45%,#f4f0e6,#e4dcc8 50%,#6a9a4a)"></div>Califlower</div>
    <div class="food"><div class="food-photo" role="img" aria-label="Photo of tomatoes" style="background:radial-gradient(circle,#e0301e 45%,#b81812 60%,#fff 75%)"></div>Tomato</div>
  </div>

  <div class="food-row-last">
    <div class="food" style="left:63px"><div class="food-photo" role="img" aria-label="Photo of a dairy cow" style="background:linear-gradient(#f0f0f0,#d8d8d8 55%,#5a8a3a)"></div>Cow</div>
    <div class="food" style="left:215px;gap:15px"><div class="food-photo" role="img" aria-label="Photo of a halibut" style="background:radial-gradient(ellipse 50% 35%,#8a5a3a 80%,#fff 100%)"></div>Halibut</div>
    <div class="food" style="left:386px;gap:14px"><div class="food-photo" role="img" aria-label="Photo of a fish" style="background:radial-gradient(ellipse 50% 40%,#5a6a6a 80%,#fff 100%)"></div>Fish</div>
  </div>

  <div class="foods-foot"></div>
</section>

<section class="sheet sheet--symptoms">
  <div class="rule"></div>
  <h2 class="symptoms-pill">Symptoms of Anemia</h2>

  <svg class="wave" width="551" height="707" viewBox="0 0 551 707" aria-hidden="true">
    <defs>
      <linearGradient id="tealFill" x1="0" x2="1"><stop offset="0" stop-color="#0d7f73"/><stop offset="1" stop-color="#10a394"/></linearGradient>
    </defs>
    <path d="M0,329 C90,360 170,378 245,388 L0,392 Z" fill="var(--maroon)"/>
    <path d="M0,378 C160,398 390,382 551,322 L551,707 L0,707 Z" fill="#fff"/>
    <path d="M0,381 C160,401 390,385 551,325 L551,707 L0,707 Z" fill="url(#tealFill)"/>
  </svg>

  <svg width="0" height="0" style="position:absolute" aria-hidden="true">
    <defs>
      <linearGradient id="fatigueTone" x1="0" y1="0" x2="0" y2="1"><stop offset="0" stop-color="#eae4de"/><stop offset=".35" stop-color="#6a4430"/><stop offset=".65" stop-color="#2c3a5a"/><stop offset="1" stop-color="#a0704a"/></linearGradient>
      <linearGradient id="headacheTone" x1="0" y1="0" x2="1" y2="1"><stop offset="0" stop-color="#dcd8d4"/><stop offset=".5" stop-color="#c09a84"/><stop offset="1" stop-color="#4a6a9a"/></linearGradient>
      <radialGradient id="dizzyTone"><stop offset="0" stop-color="#a06a50"/><stop offset=".6" stop-color="#5a3828"/><stop offset="1" stop-color="#2a1c16"/></radialGradient>
      <linearGradient id="visionTone" x1="0" y1="0" x2="1" y2="0"><stop offset="0" stop-color="#e8d0c0"/><stop offset=".4" stop-color="#8a6a5a"/><stop offset="1" stop-color="#2a4a5a"/></linearGradient>
      <linearGradient id="muscleTone" x1="0" y1="0" x2="1" y2="1"><stop offset="0" stop-color="#f4ece6"/><stop offset=".5" stop-color="#e8c8b4"/><stop offset="1" stop-color="#f0e8e2"/></linearGradient>
    </defs>
  </svg>

  <div class="symptom" style="left:83px;top:137px">
    <svg class="symptom-ring" width="130" height="130" viewBox="0 0 130 130"><circle cx="69" cy="58" r="56" fill="var(--maroon)"/><circle cx="60" cy="60" r="56" fill="#fff"/><circle cx="60" cy="60" r="55" fill="var(--teal)"/><circle cx="60" cy="60" r="51" fill="url(#fatigueTone)" role="img" aria-label="Photo of a tired woman resting her head on a table"/></svg>
  </div>
  <div class="symptom" style="left:269px;top:140px">
    <svg class="symptom-ring" width="130" height="130" viewBox="0 0 130 130"><circle cx="69" cy="58" r="56" fill="var(--maroon)"/><circle cx="60" cy="60" r="56" fill="#fff"/><circle cx="60" cy="60" r="55" fill="var(--teal)"/><circle cx="60" cy="60" r="51" fill="url(#headacheTone)" role="img" aria-label="Photo of a man holding his head with a headache"/></svg>
  </div>
  <div class="symptom" style="left:449px;top:137px">
    <svg class="symptom-ring" width="130" height="130" viewBox="0 0 130 130"><circle cx="69" cy="58" r="56" fill="var(--maroon)"/><circle cx="60" cy="60" r="56" fill="#fff"/><circle cx="60" cy="60" r="55" fill="var(--teal)"/><circle cx="60" cy="60" r="51" fill="url(#dizzyTone)" role="img" aria-label="Photo of a dizzy woman covering her face"/></svg>
  </div>
  <div class="symptom" style="left:166px;top:267px">
    <svg class="symptom-ring" width="130" height="130" viewBox="0 0 130 130"><circle cx="69" cy="58" r="56" fill="var(--maroon)"/><circle cx="60" cy="60" r="56" fill="#fff"/><circle cx="60" cy="60" r="55" fill="var(--teal)"/><circle cx="60" cy="60" r="51" fill="url(#visionTone)" role="img" aria-label="Photo of a person rubbing their eyes while holding glasses"/></svg>
  </div>
  <div class="symptom" style="left:359px;top:273px">
    <svg class="symptom-ring" width="130" height="130" viewBox="0 0 130 130"><circle cx="69" cy="58" r="56" fill="var(--maroon)"/><circle cx="60" cy="60" r="56" fill="#fff"/><circle cx="60" cy="60" r="55" fill="var(--teal)"/><circle cx="60" cy="60" r="51" fill="url(#muscleTone)" role="img" aria-label="Photo of a hand holding a sore wrist"/></svg>
  </div>

  <span class="symptom-label" style="left:86px;top:199px">Fatigue</span>
  <span class="symptom-label" style="left:275px;top:202px">Headache</span>
  <span class="symptom-label" style="left:452px;top:199px">Dizziness</span>
  <span class="symptom-label" style="left:165px;top:327px">Blurry Vision</span>
  <span class="symptom-label" style="left:358px;top:330px">Muscle Weakness</span>

  <div class="signs-line" style="left:55px;width:101px"></div>
  <h2 class="signs-title">Signs of Anemia</h2>
  <div class="signs-line" style="left:390px;width:102px"></div>

  <div class="sign" style="left:84px;top:505px"><div class="sign-photo" role="img" aria-label="Photo of a pale hand beside a normal hand" style="background:linear-gradient(90deg,#b07a6e,#c8968a 30%,#ece6e2 45%,#e8e4e0 60%,#c89484 80%,#a87060)"></div></div>
  <div class="sign" style="left:259px;top:515px"><div class="sign-photo" role="img" aria-label="Photo of pale, brittle fingernails" style="background:linear-gradient(90deg,#c8c0c0,#b8a4a4 25%,#8a5a6a 55%,#c4b4b4 80%,#e8e4e4)"></div></div>
  <div class="sign" style="left:445px;top:513px"><div class="sign-photo" role="img" aria-label="Photo of a red inner eyelid above a pale inner eyelid" style="background:linear-gradient(#f0e8e6 8%,#4a3a30 22%,#d86a74 38%,#a87068 46%,#ffffff 48%,#ffffff 56%,#c8c0b8 60%,#7a8a9a 68%,#e4b8b0 82%,#ffffff 92%)"></div></div>
  <div class="sign" style="left:165px;top:621px"><div class="sign-photo" role="img" aria-label="Photo of a red tongue beside a pale tongue" style="background:linear-gradient(90deg,#c4908a,#d67a7c 25%,#8a5a54 49%,#ffffff 50%,#ffffff 52%,#d8a8a0 53%,#e8b8b4 75%,#c49488)"></div></div>
  <div class="sign" style="left:351px;top:621px"><div class="sign-photo" role="img" aria-label="Photo of a pale palm beside a normal palm" style="background:linear-gradient(90deg,#f0f0ee,#e8cc8a 20%,#e0c070 45%,#c8a08a 60%,#a87a6a 85%,#d8d8d8)"></div></div>
</section>

</body>
</html>
```